Trade show Banner to be displayed on vertical stand

We are an IT company that specializes in working with Manufacturing companies and manufacturing plants. We need two banners designed for a manufacturing trade show. The design needs to be designed using the supplied template file. Also the design needs to communicate graphically that we specialize in working with manufacturing plants. Also they should communicate that out services include: IT Services, Network, Voice, Data

Target Market(s)

Manufacturing companies

Industry/Entity Type

Manufacturing

Requirements
Must have
• Clear message, clear graphic message. Must be designed with included templates
Nice to have
• Company colors need to be used, but additional colors can be used

```html
<!DOCTYPE html>
<html lang="en">
<head>
<meta charset="utf-8">
<title>linkwise systems – trade show banners</title>
<link rel="stylesheet" href="https://fonts.googleapis.com/css2?family=Oswald:wght@400;500&family=Open+Sans:wght@600;700&display=swap">
<style>
  :root {
    --brand-blue: #2a78c2;
    --brand-blue-deep: #1f66ad;
    --sky: #8fc3ea;
    --orange: #f08a24;
    --orange-soft: #f39a3f;
    --ink: #1d1d1d;
    --paper: #ffffff;
    --backdrop: #ececec;
  }
  * { box-sizing: border-box; margin: 0; padding: 0; }
  html, body { width: 1112px; height: 1200px; overflow: hidden; }
  body {
    background: var(--backdrop);
    font-family: "Oswald", "Arial Narrow", sans-serif;
    position: relative;
  }
  .banner {
    position: absolute;
    top: 140px;
    width: 320px;
    height: 920px;
    background: var(--paper);
    overflow: hidden;
    box-shadow: 0 6px 24px rgba(0,0,0,.12);
  }
  .banner--intro { left: 196px; }
  .banner--services { left: 596px; }
  .layer { position: absolute; left: 0; top: 0; width: 320px; height: 920px; }

  .brand {
    position: absolute;
    display: flex;
    align-items: center;
    gap: 10px;
  }
  .brand__dot {
    width: 40px; height: 40px; border-radius: 50%;
  }
  .brand__name {
    font-family: "Oswald", "Arial Narrow", sans-serif;
    font-weight: 500;
    font-size: 30px;
    line-height: 1;
    letter-spacing: .5px;
  }
  .banner--intro .brand { left: 24px; top: 52px; }
  .banner--intro .brand__dot { background: var(--brand-blue); }
  .banner--intro .brand__name { color: var(--brand-blue); }
  .banner--services .brand { left: 50px; top: 748px; }
  .banner--services .brand__dot { background: var(--paper); }
  .banner--services .brand__name { color: var(--paper); }

  .support-badge {
    position: absolute;
    border-radius: 50%;
    background: var(--orange-soft);
    color: var(--paper);
    display: flex;
    flex-direction: column;
    align-items: center;
    justify-content: center;
    font-size: 23px;
    line-height: 1.3;
    text-align: center;
  }
  .support-badge__pip {
    position: absolute;
    border-radius: 50%;
    background: var(--orange-soft);
  }
  .banner--intro .support-badge { left: -8px; top: 430px; width: 128px; height: 128px; }
  .banner--intro .support-badge__pip { left: 80px; top: 550px; width: 32px; height: 32px; }
  .banner--services .support-badge { left: 188px; top: 218px; width: 130px; height: 130px; }
  .banner--services .support-badge__pip { left: 168px; top: 312px; width: 34px; height: 34px; }

  .headline {
    position: absolute;
    left: 24px;
    top: 620px;
    color: var(--paper);
    font-size: 27px;
    line-height: 1.55;
    letter-spacing: .2px;
    font-weight: 400;
  }
  .headline em { font-style: normal; color: var(--orange); }

  .web-pill {
    position: absolute;
    left: 50%;
    transform: translateX(-50%);
    background: var(--orange);
    color: var(--paper);
    font-family: "Open Sans", Arial, sans-serif;
    font-weight: 700;
    font-size: 15px;
    letter-spacing: 1.5px;
    padding: 4px 18px;
    border-radius: 12px;
    white-space: nowrap;
  }
  .banner--intro .web-pill { top: 790px; }
  .banner--services .web-pill { top: 820px; }

  .services-title {
    position: absolute;
    top: 368px;
    width: 100%;
    text-align: center;
    font-size: 28px;
    font-weight: 500;
    color: var(--ink);
    letter-spacing: .5px;
  }
  .services-title span { color: var(--brand-blue); }
  .services-title__rule {
    position: absolute;
    top: 418px;
    left: 72px;
    width: 176px;
    height: 2px;
    background: var(--orange);
  }
  .service-grid {
    position: absolute;
    top: 448px;
    left: 14px;
    width: 292px;
    display: grid;
    grid-template-columns: repeat(4, 1fr);
    row-gap: 26px;
  }
  .service {
    display: flex;
    flex-direction: column;
    align-items: center;
    text-align: center;
  }
  .service__icon {
    width: 44px; height: 44px;
    border: 2px solid var(--orange);
    border-radius: 50%;
    display: flex; align-items: center; justify-content: center;
  }
  .service__icon svg { width: 24px; height: 24px; }
  .service__label {
    margin-top: 6px;
    font-size: 11.5px;
    line-height: 1.5;
    color: var(--brand-blue);
    text-transform: uppercase;
  }
</style>
</head>
<body>

  <!-- Banner one: headline and support promise -->
  <section class="banner banner--intro">
    <svg class="layer" viewBox="0 0 320 920" aria-hidden="true">
      <path d="M0 166 Q160 122 320 166 L320 182 Q160 140 0 184 Z" fill="var(--sky)"/>
      <path d="M0 548 Q160 498 320 528 L320 920 L0 920 Z" fill="var(--sky)"/>
      <path d="M0 562 Q160 512 320 544 L320 920 L0 920 Z" fill="var(--brand-blue)"/>
    </svg>
    <svg class="layer" viewBox="0 0 320 920" role="img" aria-label="Photo: plant technician in hard hat and safety vest checking a tablet on the factory floor">
      <defs>
        <linearGradient id="plantFloor" x1="0" y1="0" x2="1" y2="1">
          <stop offset="0" stop-color="#5a5146"/>
          <stop offset=".45" stop-color="#8a6a3e"/>
          <stop offset=".75" stop-color="#8ea23b"/>
          <stop offset="1" stop-color="#3b3a35"/>
        </linearGradient>
      </defs>
      <path d="M0 184 Q160 142 320 182 L320 528 Q160 498 0 548 Z" fill="url(#plantFloor)"/>
    </svg>

    <div class="brand">
      <span class="brand__dot"></span>
      <span class="brand__name">linkwise systems</span>
    </div>

    <div class="support-badge"><span>24x7</span><span>SUPPORT</span></div>
    <div class="support-badge__pip"></div>

    <h1 class="headline">WE <em>MAXIMIZE PRODUCTION</em><br><em>UPTIME</em> BY REDUCING<br>NETWORK DOWNTIME</h1>

    <div class="web-pill">WWW.LWSYS.COM</div>
  </section>

  <!-- Banner two: service overview -->
  <section class="banner banner--services">
    <svg class="layer" viewBox="0 0 320 920" aria-hidden="true">
      <path d="M0 318 Q160 348 320 306 L320 322 Q160 362 0 334 Z" fill="var(--sky)"/>
      <path d="M0 720 Q160 676 320 706 L320 920 L0 920 Z" fill="var(--sky)"/>
      <path d="M0 736 Q160 690 320 722 L320 920 L0 920 Z" fill="var(--brand-blue)"/>
    </svg>
    <svg class="layer" viewBox="0 0 320 920" role="img" aria-label="Photo: engineer in blue coveralls and hard hat working on a laptop beside plant control panels">
      <defs>
        <linearGradient id="controlRoom" x1="0" y1="0" x2="1" y2="1">
          <stop offset="0" stop-color="#1e4f9a"/>
          <stop offset=".5" stop-color="#2f6fc0"/>
          <stop offset="1" stop-color="#9db4c8"/>
        </linearGradient>
      </defs>
      <path d="M0 0 H320 V306 Q160 348 0 318 Z" fill="url(#controlRoom)"/>
    </svg>

    <div class="support-badge"><span>24x7</span><span>SUPPORT</span></div>
    <div class="support-badge__pip"></div>

    <h2 class="services-title">WHAT WE <span>DO</span></h2>
    <div class="services-title__rule"></div>

    <div class="service-grid">
      <div class="service">
        <div class="service__icon">
          <svg viewBox="0 0 24 24" fill="none" stroke="var(--orange)" stroke-width="2"><circle cx="12" cy="12" r="3.5"/><path d="M12 2v4M12 18v4M2 12h4M18 12h4M4.9 4.9l2.8 2.8M16.3 16.3l2.8 2.8M4.9 19.1l2.8-2.8M16.3 7.7l2.8-2.8"/></svg>
        </div>
        <span class="service__label">Managed IT<br>Service</span>
      </div>
      <div class="service">
        <div class="service__icon">
          <svg viewBox="0 0 24 24" fill="none" stroke="var(--orange)" stroke-width="2" stroke-linecap="round"><path d="M3 9.5a13 13 0 0 1 18 0M6 13a8.5 8.5 0 0 1 12 0M9 16.5a4 4 0 0 1 6 0"/><circle cx="12" cy="19.5" r="1" fill="var(--orange)"/></svg>
        </div>
        <span class="service__label">Wireless<br>Network</span>
      </div>
      <div class="service">
        <div class="service__icon">
          <svg viewBox="0 0 24 24" fill="none" stroke="var(--orange)" stroke-width="2"><path d="M3 6h18"/><path d="M5 6v3a7 7 0 0 0 14 0V6"/><circle cx="12" cy="10" r="2.5"/></svg>
        </div>
        <span class="service__label">CCTV<br>Surveillance</span>
      </div>
      <div class="service">
        <div class="service__icon">
          <svg viewBox="0 0 24 24" fill="none" stroke="var(--orange)" stroke-width="2"><ellipse cx="12" cy="5.5" rx="7" ry="2.5"/><path d="M5 5.5v13c0 1.4 3.1 2.5 7 2.5s7-1.1 7-2.5v-13M5 10c0 1.4 3.1 2.5 7 2.5s7-1.1 7-2.5M5 14.5c0 1.4 3.1 2.5 7 2.5s7-1.1 7-2.5"/></svg>
        </div>
        <span class="service__label">Data<br>Backup</span>
      </div>
      <div class="service">
        <div class="service__icon">
          <svg viewBox="0 0 24 24" fill="none" stroke="var(--orange)" stroke-width="2.4" stroke-linecap="round"><path d="M5 5l14 14M19 5L5 19"/></svg>
        </div>
        <span class="service__label">Projects</span>
      </div>
      <div class="service">
        <div class="service__icon">
          <svg viewBox="0 0 24 24"><path d="M7 18a4 4 0 0 1-.6-8 5.5 5.5 0 0 1 10.7-1A4.5 4.5 0 0 1 17.5 18Z" fill="var(--orange)"/></svg>
        </div>
        <span class="service__label">Cloud</span>
      </div>
      <div class="service">
        <div class="service__icon">
          <svg viewBox="0 0 24 24" fill="none" stroke="var(--orange)" stroke-width="2" stroke-linecap="round"><rect x="9" y="3" width="6" height="11" rx="3"/><path d="M6 11a6 6 0 0 0 12 0M12 17v4M9 21h6"/></svg>
        </div>
        <span class="service__label">Voice</span>
      </div>
      <div class="service">
        <div class="service__icon">
          <svg viewBox="0 0 24 24" fill="none" stroke="var(--orange)" stroke-width="2"><path d="M7 13a3.5 3.5 0 0 1-.4-7 4.5 4.5 0 0 1 8.8-.8A3.6 3.6 0 0 1 17 13Z" fill="var(--orange)"/><path d="M12 13v4M7 17h10M7 17v3M17 17v3M12 17v3"/></svg>
        </div>
        <span class="service__label">Virtualization</span>
      </div>
    </div>

    <div class="brand">
      <span class="brand__dot"></span>
      <span class="brand__name">linkwise systems</span>
    </div>

    <div class="web-pill">WWW.LWSYS.COM</div>
  </section>

</body>
</html>
```